I'm a one-man show, working as management consultant, project manager and offering personal coaching .
The logo should contain my name, and "management consultant" as a subtitle. My aim is to appear professional and kind of exclusive, but in a "casual" and dynamic way.
My aim is to implement new ideas in a holistic approach.
The colours preferred are black and shades of blue and violet, on a white background.

Contact Information for Business Card

I would like to have a white front, and a creative backside.
it would be awesome it the logo itself can be minted / stamped.

Besides my name, the business card should contain my operations, meaning
management consultant
project management
personal coaching

Logo Text

Matthias Brenner - Management Consultant

Colors
886aae
0456a4
ffffff
33a6d7

Requirements
Must have
• a creative and catchy logo
• I would appreciate the profile of an eagle as a small symbol besides my name at the logo

```html
<!DOCTYPE html>
<html lang="de">
<head>
<meta charset="utf-8">
<title>Matthias Brenner – Business Card</title>
<link rel="stylesheet" href="https://fonts.googleapis.com/css2?family=Roboto:wght@400;700&display=swap">
<style>
  :root {
    --ink: #2a2a2c;
    --card-dark: #2b2b2e;
    --paper: #ffffff;
    --blue: #0456a4;
    --violet: #8a2aa8;
    --violet-soft: #886aae;
    --muted: #555559;
    --stage: #e6e6e8;
  }
  * { box-sizing: border-box; margin: 0; padding: 0; }
  html, body { width: 1200px; height: 1000px; overflow: hidden; }
  body {
    background: var(--stage);
    font-family: "Roboto", Arial, sans-serif;
    display: flex;
    align-items: center;
    justify-content: center;
    gap: 60px;
  }
  .card {
    position: relative;
    width: 500px;
    height: 286px;
    border-radius: 4px;
    overflow: hidden;
    box-shadow: 0 10px 30px rgba(0,0,0,.18);
  }
  .card-front { background: var(--paper); }
  .card-back { background: var(--card-dark); }
  .front-swoosh { position: absolute; inset: 0; width: 100%; height: 100%; }

  .brand { display: flex; align-items: center; gap: 12px; }
  .brand-dot {
    width: 34px; height: 34px; border-radius: 50%;
    background: var(--violet-soft);
    flex: none;
  }
  .brand-name {
    font-size: 19px; font-weight: 400; letter-spacing: 1px;
    line-height: 1.05; text-transform: uppercase;
  }
  .brand-sub { font-size: 10px; margin-top: 3px; }

  .front-content {
    position: absolute;
    left: 188px; top: 34px;
    color: var(--ink);
  }
  .front-content .brand-name { color: var(--ink); }
  .front-content .brand-sub { color: var(--muted); }
  .person-name { font-size: 21px; font-weight: 700; margin-top: 22px; white-space: nowrap; }
  .person-role { font-size: 12px; color: var(--muted); margin-top: 4px; }
  .contact-list {
    list-style: none; margin-top: 14px;
    font-size: 12px; color: var(--muted); line-height: 1.9;
  }
  .contact-list li { display: inline-block; margin-right: 10px; white-space: nowrap; }
  .contact-list li::before {
    content: ""; display: inline-block;
    width: 5px; height: 5px; border-radius: 50%;
    background: var(--violet);
    margin-right: 5px; vertical-align: middle;
  }
  .contact-list .contact-address { display: block; }

  .back-content {
    position: absolute; inset: 0;
    display: flex; align-items: center; justify-content: center;
  }
  .back-content .brand-name { color: var(--paper); }
  .back-content .brand-sub { color: #d8d8dc; }
</style>
</head>
<body>

<section class="card card-front" aria-label="Business card front">
  <svg class="front-swoosh" viewBox="0 0 500 286" aria-hidden="true">
    <defs>
      <linearGradient id="swooshGradient" x1="0" y1="0" x2="1" y2="1">
        <stop offset="0" stop-color="#0456a4"/>
        <stop offset="1" stop-color="#8a2aa8"/>
      </linearGradient>
    </defs>
    <path d="M0 0 H50 Q60 170 300 286 H0 Z" fill="var(--card-dark)"/>
    <path d="M50 0 Q60 170 300 286 H280 Q46 178 36 0 Z" fill="url(#swooshGradient)"/>
  </svg>
  <div class="front-content">
    <div class="brand">
      <span class="brand-dot"></span>
      <div>
        <div class="brand-name">Matthias<br>Brenner</div>
        <div class="brand-sub">Management Consultant</div>
      </div>
    </div>
    <div class="person-name">Mag. (FH) Matthias Brenner</div>
    <div class="person-role">Management Consultant</div>
    <ul class="contact-list">
      <li>+43 660 4817392</li>
      <li>office@brenner-consult.at</li>
      <li class="contact-address">Lindenweg 12, 5020 Salzburg</li>
    </ul>
  </div>
</section>

<section class="card card-back" aria-label="Business card back">
  <div class="back-content">
    <div class="brand">
      <span class="brand-dot"></span>
      <div>
        <div class="brand-name">Matthias<br>Brenner</div>
        <div class="brand-sub">Management Consultant</div>
      </div>
    </div>
  </div>
</section>

</body>
</html>
```